Pelverhook LLC
Business Cards & Stationary
Professional
Tobias Wendell
President
482 Orchard Crest Road
Dunmore Falls, NJ 07934-2718
tobias.wendell@mailvexo.com
www.pelverhook.com
I require the full suite of stationary products i.e.:- Business card, letterhead, envelope, fax cover sheet, thank you cards, invoice etc.
Just the logo on the back of the card.

```html
<!DOCTYPE html>
<html lang="en">
<head>
<meta charset="utf-8">
<title>Pelverhook LLC — Stationery Suite</title>
<link href="https://fonts.googleapis.com/css2?family=Open+Sans:wght@400;600;700&display=swap" rel="stylesheet">
<style>
  :root {
    --stage: #e8e5e0;
    --paper: #ffffff;
    --brand-blue: #1f5fae;
    --brand-blue-light: #4a8fd6;
    --brand-blue-dark: #163f7a;
    --ink: #3a4350;
    --ink-soft: #7c8794;
    --caption: #6d6a66;
    --envelope-grey: #8d9096;
    --faint: rgba(31, 95, 174, 0.07);
  }
  * { box-sizing: border-box; margin: 0; padding: 0; }
  html, body { width: 1200px; height: 413px; overflow: hidden; }
  body {
    background: var(--stage);
    font-family: "Open Sans", Arial, sans-serif;
    color: var(--ink);
    position: relative;
  }
  .piece {
    position: absolute;
    background: var(--paper);
    box-shadow: 0 2px 6px rgba(0,0,0,0.25);
    overflow: hidden;
  }
  .caption {
    position: absolute;
    font-size: 6px;
    color: var(--caption);
    text-align: center;
    letter-spacing: 0.2px;
  }
  .wordmark {
    display: flex;
    align-items: center;
    gap: 4px;
    font-weight: 700;
    color: var(--brand-blue);
    letter-spacing: 0.5px;
    text-transform: uppercase;
  }
  .wordmark .dot {
    border-radius: 50%;
    background: var(--brand-blue);
    flex: none;
  }
  .wordmark.on-blue { color: #fff; }
  .wordmark.on-blue .dot { background: #fff; }

  /* Business cards */
  .card { left: 91px; width: 125px; height: 66px; border-radius: 4px; }
  .card-front { top: 100px; }
  .card-front .wordmark { position: absolute; left: 8px; top: 20px; font-size: 6.5px; }
  .card-front .wordmark .dot { width: 9px; height: 9px; }
  .card-front .contact {
    position: absolute; right: 7px; top: 12px; width: 58px;
    font-size: 3.6px; line-height: 5.2px; color: var(--ink);
  }
  .card-front .contact .name { font-weight: 700; font-size: 4.4px; color: var(--brand-blue); }
  .card-front .web {
    position: absolute; left: 0; right: 0; bottom: 0; height: 11px;
    background: linear-gradient(90deg, var(--brand-blue-dark), var(--brand-blue-light));
    color: #fff; font-size: 3.6px; line-height: 11px; text-align: center;
  }
  .card-back-white { top: 235px; }
  .card-back-white .wordmark { position: absolute; right: 8px; top: 28px; font-size: 6.5px; }
  .card-back-white .wordmark .dot { width: 9px; height: 9px; }
  .card-back-white .faint-disc {
    position: absolute; left: -14px; top: -8px; width: 70px; height: 70px;
    border-radius: 50%; background: var(--faint);
  }
  .card-back-blue {
    top: 320px; height: 66px;
    background: linear-gradient(135deg, var(--brand-blue-dark), var(--brand-blue-light));
  }
  .card-back-blue .wordmark { position: absolute; left: 10px; top: 28px; font-size: 6.5px; }
  .card-back-blue .wordmark .dot { width: 9px; height: 9px; }

  /* Letterheads */
  .letterhead { top: 18px; width: 268px; height: 362px; }
  .letterhead-first { left: 259px; }
  .letterhead-second { left: 547px; }
  .letterhead-band {
    position: absolute; left: 0; right: 0; top: 0; height: 44px;
    background: linear-gradient(90deg, var(--brand-blue-dark), var(--brand-blue) 45%, var(--brand-blue-light));
  }
  .letterhead-band .logo-tab {
    position: absolute; left: 12px; top: 0; width: 88px; height: 48px;
    background: var(--paper); border-radius: 0 0 6px 6px;
    box-shadow: 0 1px 3px rgba(0,0,0,0.2);
  }
  .letterhead-band .logo-tab .wordmark {
    position: absolute; left: 8px; top: 19px; font-size: 7px;
  }
  .letterhead-band .logo-tab .dot { width: 10px; height: 10px; }
  .letterhead-band .header-contact {
    position: absolute; right: 12px; top: 10px;
    font-size: 3.8px; line-height: 5.4px; color: #fff; text-align: left;
  }
  .letterhead .watermark {
    position: absolute; left: 74px; top: 262px; width: 120px; height: 120px;
    border-radius: 50%; background: var(--faint);
  }
  .letterhead .watermark-name {
    position: absolute; left: 0; right: 0; top: 300px;
    text-align: center; font-weight: 700; font-size: 14px;
    color: rgba(31, 95, 174, 0.08); letter-spacing: 1px; text-transform: uppercase;
  }
  .letterhead-footer {
    position: absolute; left: 0; right: 0; bottom: 8px;
    font-size: 3.6px; text-align: center; color: var(--ink-soft);
  }

  /* Envelopes */
  .envelope { border-radius: 2px; }
  .envelope-back {
    left: 880px; top: 22px; width: 300px; height: 128px; background: #f4f5f7;
  }
  .envelope-back svg { position: absolute; inset: 0; }
  .envelope-back .wordmark {
    position: absolute; left: 0; right: 0; top: 26px; justify-content: center;
    font-size: 7px; color: #fff;
  }
  .envelope-back .wordmark .dot { width: 10px; height: 10px; background: #fff; }
  .envelope-flap-blue {
    left: 893px; top: 100px; width: 300px; height: 118px; background: #f4f5f7;
  }
  .envelope-flap-blue svg { position: absolute; inset: 0; }
  .envelope-flap-blue .wordmark {
    position: absolute; left: 0; right: 0; top: 22px; justify-content: center; font-size: 7px;
  }
  .envelope-flap-blue .wordmark .dot { width: 10px; height: 10px; }
  .envelope-front {
    left: 852px; top: 172px; width: 270px; height: 124px;
  }
  .envelope-front .wordmark { position: absolute; left: 12px; top: 12px; font-size: 6.5px; }
  .envelope-front .wordmark .dot { width: 9px; height: 9px; }
  .envelope-front .return {
    position: absolute; left: 12px; top: 26px; font-size: 3.6px; line-height: 5px; color: var(--ink-soft);
  }
  .envelope-front .base {
    position: absolute; left: 0; right: 0; bottom: 0; height: 14px;
    background: linear-gradient(90deg, var(--brand-blue-dark), var(--brand-blue-light));
    color: #fff; font-size: 3.6px; line-height: 14px; padding-left: 12px;
  }
  .envelope-blue {
    left: 833px; top: 240px; width: 200px; height: 124px;
    background: linear-gradient(135deg, var(--brand-blue-dark), var(--brand-blue-light));
  }
  .envelope-blue .wordmark { position: absolute; left: 12px; top: 12px; font-size: 6.5px; }
  .envelope-blue .wordmark .dot { width: 9px; height: 9px; }
  .envelope-blue .return {
    position: absolute; left: 12px; top: 26px; font-size: 3.6px; line-height: 5px; color: #dfe9f7;
  }
</style>
</head>
<body>

  <!-- Business cards -->
  <section class="piece card card-front">
    <div class="wordmark"><span class="dot"></span>Pelverhook</div>
    <div class="contact">
      <div class="name">Tobias Wendell</div>
      <div>President</div>
      <div>482 Orchard Crest Road</div>
      <div>Dunmore Falls, NJ 07934-2718</div>
      <div>tobias.wendell@mailvexo.com</div>
    </div>
    <div class="web">www.pelverhook.com</div>
  </section>
  <div class="caption" style="left:91px;top:171px;width:125px;">Card front</div>

  <section class="piece card card-back-white">
    <div class="faint-disc"></div>
    <div class="wordmark"><span class="dot"></span>Pelverhook</div>
  </section>
  <div class="caption" style="left:91px;top:305px;width:125px;">Card back</div>

  <section class="piece card card-back-blue">
    <div class="wordmark on-blue"><span class="dot"></span>Pelverhook</div>
  </section>
  <div class="caption" style="left:91px;top:391px;width:125px;">Card reverse</div>

  <!-- Letterheads -->
  <section class="piece letterhead letterhead-first">
    <header class="letterhead-band">
      <div class="logo-tab"><div class="wordmark"><span class="dot"></span>Pelverhook</div></div>
      <div class="header-contact">
        <div>482 Orchard Crest Road</div>
        <div>Dunmore Falls, NJ 07934-2718</div>
        <div>tobias.wendell@mailvexo.com</div>
        <div>www.pelverhook.com</div>
      </div>
    </header>
    <div class="watermark"></div>
    <div class="watermark-name">Pelverhook</div>
  </section>
  <div class="caption" style="left:259px;top:386px;width:268px;">Letterhead first</div>

  <section class="piece letterhead letterhead-second">
    <div class="watermark"></div>
    <div class="watermark-name">Pelverhook</div>
    <footer class="letterhead-footer">482 Orchard Crest Road · Dunmore Falls, NJ 07934-2718 · www.pelverhook.com</footer>
  </section>
  <div class="caption" style="left:547px;top:386px;width:268px;">Letterhead second</div>

  <!-- Envelopes -->
  <section class="piece envelope envelope-back">
    <svg width="300" height="128" viewBox="0 0 300 128" aria-hidden="true">
      <polygon points="0,0 300,0 150,78" fill="var(--envelope-grey)"/>
      <polyline points="0,128 150,62 300,128" fill="none" stroke="#d8dbe0" stroke-width="1"/>
    </svg>
    <div class="wordmark"><span class="dot"></span>Pelverhook</div>
  </section>

  <section class="piece envelope envelope-flap-blue">
    <svg width="300" height="118" viewBox="0 0 300 118" aria-hidden="true">
      <defs>
        <linearGradient id="flapBlue" x1="0" y1="0" x2="1" y2="0">
          <stop offset="0" stop-color="#163f7a"/>
          <stop offset="1" stop-color="#4a8fd6"/>
        </linearGradient>
      </defs>
      <polygon points="0,0 300,0 150,72" fill="url(#flapBlue)"/>
      <polyline points="0,118 150,58 300,118" fill="none" stroke="#d8dbe0" stroke-width="1"/>
    </svg>
    <div class="wordmark on-blue"><span class="dot"></span>Pelverhook</div>
  </section>

  <section class="piece envelope envelope-front">
    <div class="wordmark"><span class="dot"></span>Pelverhook</div>
    <div class="return">
      <div>482 Orchard Crest Road</div>
      <div>Dunmore Falls, NJ 07934-2718</div>
    </div>
    <div class="base">www.pelverhook.com</div>
  </section>

  <section class="piece envelope envelope-blue">
    <div class="wordmark on-blue"><span class="dot"></span>Pelverhook</div>
    <div class="return">
      <div>482 Orchard Crest Road</div>
      <div>Dunmore Falls, NJ 07934-2718</div>
    </div>
  </section>
  <div class="caption" style="left:833px;top:386px;width:200px;">Envelope set</div>

</body>
</html>
```